Quenlo needs a CD cover artwork for the song "Quiet Harbors"

Hi, I need a CD cover artwork for my new song "Quiet Harbors". I want to have an image of "Earth" for it. The earth image can be either picturesque or unique artistic. And also, it needs to contain the logo "Quenlo" and "Quiet Harbors".
jpg. file is necessary.
And I don't like something purchased from the stock image which I need to pay additionally. Original image is preferable.

Target Market(s)

Music

Colors

Designer to choose colors to be used in the design.

Requirements
Must have
• -Earth image
• -The logo "Quenlo" and "Quiet Harbors"
Nice to have
• -A whole globe image of the earth might be good, rather than a part of the globe or scene of the earth.
• -Something awe-inspiring image might be good.
• -The logo "Quenlo" and "Quiet Harbors" better fuse to the image nicely rather than oddly standing out from the image.
Should not have
• -the stock image which I need to pay additionally

```html
<!DOCTYPE html>
<html lang="en">
<head>
<meta charset="utf-8">
<title>Quenlo – Quiet Harbors</title>
<link rel="stylesheet" href="https://fonts.googleapis.com/css2?family=Big+Shoulders+Display:wght@700;800&display=swap">
<style>
  :root {
    --paper-top: #f2f2f4;
    --paper-bottom: #d9d8dc;
    --teal-light: #19b3c4;
    --teal-mid: #1f9aa6;
    --teal-deep: #36777c;
    --globe-glow: #2fd0dd;
    --globe-core: #1b4f58;
    --globe-shadow: #12262c;
    --globe-cloud: #c9cbd2;
    --ink: #0e1826;
  }
  html, body {
    margin: 0;
    padding: 0;
    width: 1200px;
    height: 1200px;
    overflow: hidden;
  }
  .cover {
    position: relative;
    width: 1200px;
    height: 1200px;
    overflow: hidden;
    background: linear-gradient(180deg, var(--paper-top) 0%, var(--paper-bottom) 70%);
  }
  .cover__art {
    position: absolute;
    inset: 0;
    width: 1200px;
    height: 1200px;
  }
  .title-block {
    position: absolute;
    top: 104px;
    right: 100px;
    text-align: right;
    color: var(--ink);
    font-family: "Big Shoulders Display", "Arial Narrow", sans-serif;
    transform: scaleX(0.62);
    transform-origin: right top;
  }
  .title-block__artist {
    margin: 0;
    font-weight: 800;
    font-size: 150px;
    line-height: 1;
    letter-spacing: 2px;
  }
  .title-block__song {
    margin: 6px 0 0;
    font-weight: 700;
    font-size: 54px;
    line-height: 1;
    letter-spacing: 1px;
  }
</style>
</head>
<body>
  <main class="cover">
    <svg class="cover__art" viewBox="0 0 1200 1200" xmlns="http://www.w3.org/2000/svg">
      <defs>
        <linearGradient id="teal-field" x1="0" y1="0" x2="0" y2="1">
          <stop offset="0" stop-color="var(--teal-light)"/>
          <stop offset="0.55" stop-color="var(--teal-mid)"/>
          <stop offset="1" stop-color="var(--teal-deep)"/>
        </linearGradient>
        <radialGradient id="globe-tone" cx="0.38" cy="0.38" r="0.7">
          <stop offset="0" stop-color="var(--globe-glow)"/>
          <stop offset="0.45" stop-color="var(--teal-mid)"/>
          <stop offset="0.8" stop-color="var(--globe-core)"/>
          <stop offset="1" stop-color="var(--globe-shadow)"/>
        </radialGradient>
        <linearGradient id="globe-light" x1="1" y1="0" x2="0.4" y2="0.6">
          <stop offset="0" stop-color="var(--globe-cloud)" stop-opacity="0.9"/>
          <stop offset="0.35" stop-color="var(--globe-cloud)" stop-opacity="0.35"/>
          <stop offset="0.6" stop-color="var(--globe-cloud)" stop-opacity="0"/>
        </linearGradient>
      </defs>
      <polygon class="cover__teal-field" points="240,30 1200,696 1200,1200 0,1200 0,732" fill="url(#teal-field)"/>
      <g class="cover__globe" role="img" aria-label="Satellite view of the whole Earth, the Americas facing forward, tinted teal with a pale cloudy upper right">
        <circle cx="606" cy="672" r="454" fill="url(#globe-tone)"/>
        <circle cx="606" cy="672" r="454" fill="url(#globe-light)"/>
      </g>
    </svg>
    <header class="title-block">
      <h1 class="title-block__artist">Quenlo</h1>
      <p class="title-block__song">Quiet Harbors</p>
    </header>
  </main>
</body>
</html>
```